Trifold Brochure

I am looking for someone to design a marketing brochure for my construction company, We specialise in residential construction contracts which are either high end, high specification luxury homes or in volume housebuilding, i.e projects with multiple houses of apartments being built.
The format of the brochure should be A5 when folded in a trifold format
Please utilise the logo (attached), the company website (www.holvane-builds.co.uk). Please also feel free to insert any copy or images you think will be suitable.
Please also follow the guidelines below:
1. Keep it simple: Don't overload your brochure with too much text or too many images. Stick to the most important information and use bullet points or short paragraphs to make it easy for people to scan and understand.
2. Use high-quality images: Use high-resolution images that are relevant to your message and showcase your product or service in a positive light.
3. Include a call to action: Make sure your brochure includes a clear call to action, such as "Contact us today to learn more" or "Visit our website to see our full product line."
4. Use a clean, professional layout: Use a clean, uncluttered layout that is easy to read and looks professional.
5. Make it easy to read: Use a font that is easy to read and not too small.

```html
<!DOCTYPE html>
<html lang="en">
<head>
<meta charset="utf-8">
<title>Holvane Builds – Trifold Brochure</title>
<link rel="stylesheet" href="https://fonts.googleapis.com/css2?family=Montserrat:wght@300;400;500;700;800&display=swap">
<style>
:root{
  --stage:#bcbdbf;
  --navy:#13223b;
  --navy-deep:#0d1a2e;
  --gold-dark:#8b6c3c;
  --gold-light:#cdb274;
  --gold-text:#c4a563;
  --ink:#2a2f38;
  --white:#ffffff;
  --label:#8f9195;
}
*{margin:0;padding:0;box-sizing:border-box}
html,body{width:830px;height:1200px;overflow:hidden}
body{background:var(--stage);font-family:"Montserrat",sans-serif;position:relative;color:var(--white)}
.spread-label{position:absolute;left:88px;font-weight:300;font-size:20px;letter-spacing:2.5px;color:var(--label)}
.spread{position:absolute;left:88px;width:653px;display:flex;box-shadow:0 6px 14px rgba(0,0,0,.25)}
.panel{position:relative;height:100%}
.navy{background:var(--navy)}
.navy-mid{background:linear-gradient(180deg,#13233c,var(--navy-deep))}
.paper{background:linear-gradient(90deg,#fff 55%,#e4e5e7)}
.gold-band{position:absolute;background:linear-gradient(90deg,var(--gold-dark),var(--gold-light) 55%,#b39a62);display:flex;align-items:center;color:var(--white);font-weight:700}
.photo{position:absolute}
.copy{position:absolute;font-size:8.7px;line-height:12.7px;font-weight:300}
.copy.center{text-align:center}
.copy.justify{text-align:justify}
.copy p+p{margin-top:12.7px}
.dark{color:var(--ink);font-weight:400}
.brand{position:absolute;left:0;right:0;display:flex;align-items:center;justify-content:center;gap:6px}
.brand-mark{width:14px;height:14px;border:1.5px solid var(--gold-text)}
.brand-name{font-weight:400;font-size:13px;letter-spacing:2.5px;color:var(--white)}
.contact{position:absolute;left:0;right:0;text-align:center}
.phones{font-weight:700;font-size:16px;line-height:18.5px;letter-spacing:.5px}
.icon{display:block;margin:0 auto}
</style>
</head>
<body>

<div class="spread-label" style="top:68px">Front Back</div>

<section class="spread" style="top:109px;height:461px">
  <div class="panel navy" style="width:224px">
    <div class="gold-band" style="left:16px;top:18px;width:187px;height:50px;justify-content:center;font-size:15px;letter-spacing:.5px">ABOUT US</div>
    <div class="copy center" style="left:22px;top:80px;width:175px;font-size:9px;font-weight:400">
      <p>With a wealth of experience in all construction methods from steel and RC frame apartment blocks to timber frame and traditional masonry housing, we take pride in our ability to take on the most challenging and architecturally spectacular projects. No job is too big or too complex for our team of professionals.</p>
      <p>Our tradesmen are experts in their respective fields.</p>
    </div>
    <div class="photo" role="img" aria-label="Modern bedroom interior with grey stone walls and tall windows" style="left:16px;top:250px;width:187px;height:197px;background:linear-gradient(160deg,#6d6e70,#9a9896 55%,#b7ab9b)"></div>
  </div>

  <div class="panel navy-mid" style="width:218px">
    <div class="photo" role="img" aria-label="Modern white house with solar panel roof at dusk" style="left:6px;top:18px;width:193px;height:166px;background:linear-gradient(180deg,#9cb6cf,#e6e6e2 45%,#5d6b4a 80%,#2f3b3a)"></div>
    <div class="brand" style="top:208px"><span class="brand-mark"></span><span class="brand-name">HOLVANE BUILDS</span></div>
    <div class="contact" style="top:249px">
      <svg class="icon" width="14" height="14" viewBox="0 0 24 24" fill="#c4a563"><path d="M6.6 10.8a15 15 0 0 0 6.6 6.6l2.2-2.2a1 1 0 0 1 1-.25 11.4 11.4 0 0 0 3.6.57 1 1 0 0 1 1 1V20a1 1 0 0 1-1 1A17 17 0 0 1 3 4a1 1 0 0 1 1-1h3.5a1 1 0 0 1 1 1c0 1.250.2 2.450.57 3.57a1 1 0 0 1-.25 1z"/></svg>
      <div class="phones" style="margin-top:3px">07700 900418<br>020 7946 0321</div>
    </div>
    <div class="contact" style="top:314px">
      <svg class="icon" width="15" height="11" viewBox="0 0 24 18" fill="#c4a563"><path d="M0 0h24v2L12 10 0 2z"/><path d="M0 4.5l12 8 12-8V18H0z"/></svg>
      <div style="font-size:9.5px;margin-top:3px">info@holvane-builds.co.uk</div>
    </div>
    <div class="contact" style="top:354px">
      <svg class="icon" width="12" height="17" viewBox="0 0 24 34" fill="#c4a563"><path d="M12 0a12 12 0 0 0-12 12c0 9 12 22 12 22s12-13 12-22A12 12 0 0 0 12 0zm0 17a5 5 0 1 1 0-10 5 5 0 0 1 0 10z"/></svg>
      <div style="font-size:9.5px;line-height:12px;margin-top:3px">Unit 12, 40 Larkfield Road,<br>Ashbourne, AB1 2CD</div>
    </div>
    <div class="gold-band" style="left:9px;top:422px;width:187px;height:22px;justify-content:center;gap:14px">
      <span style="width:12px;height:12px;border-radius:50%;background:var(--navy)"></span>
      <span style="width:12px;height:12px;border-radius:50%;background:var(--navy)"></span>
      <span style="width:12px;height:12px;border-radius:50%;background:var(--navy)"></span>
    </div>
  </div>

  <div class="panel navy" style="width:211px">
    <div class="brand" style="top:50px"><span class="brand-mark"></span><span class="brand-name">HOLVANE BUILDS</span></div>
    <div class="gold-band" style="left:9px;top:106px;width:187px;height:22px;justify-content:center;font-size:12px;letter-spacing:1.5px"><span style="font-weight:300">LUXURY&nbsp;</span>HOMES</div>
    <div class="gold-band" style="left:9px;top:136px;width:187px;height:22px;justify-content:center;font-size:11.5px;letter-spacing:.3px">HOUSING&nbsp;<span style="font-weight:300">DEVELOPMENTS</span></div>
    <div style="position:absolute;left:0;right:0;top:164px;text-align:center;font-weight:700;font-size:10.5px;color:var(--gold-text)">A WEALTH OF EXPERIENCE</div>
    <div class="copy center" style="left:16px;top:179px;width:179px;font-size:9.3px;line-height:10.6px;font-weight:400">At Holvane Builds, we specialize in building very high specification, luxury houses and large volume residential developments for the wider housing market.</div>
    <div class="photo" role="img" aria-label="White modern villa beside an infinity pool at sunset" style="left:9px;top:245px;width:187px;height:201px;background:linear-gradient(180deg,#6f9ed0,#e8ebe9 40%,#4a91a6 70%,#5a5f62)"></div>
  </div>
</section>

<div class="spread-label" style="top:609px">Inner Pages</div>

<section class="spread" style="top:641px;height:459px">
  <div class="panel paper" style="width:218px">
    <div class="gold-band" style="left:0;top:20px;width:210px;height:22px;padding-left:20px;font-size:16px;letter-spacing:1px">FLAWLESS FINISH</div>
    <div class="copy justify dark" style="left:20px;top:51px;width:179px;font-weight:300">When searching for a construction company to complete your project, you must put your trust in the hands of true professionals to work on your property. At Holvane Builds, we are construction professionals you can trust. Our wealth of experience sets us apart from the rest. We work in the most cost-effective and efficient manner whilst maintaining an extremely high quality of work and attention to detail.</div>
    <div class="photo" role="img" aria-label="Loft living room with brick wall, fireplace and large windows" style="left:20px;top:205px;width:174px;height:238px;background:linear-gradient(160deg,#d8d6d2,#a38b72 45%,#6b6461 80%,#8d8a86)"></div>
  </div>

  <div class="panel navy-mid" style="width:217px">
    <div class="photo" role="img" aria-label="Modern apartment block with balconies against blue sky" style="left:15px;top:20px;width:187px;height:191px;background:linear-gradient(200deg,#7fb3de,#5d6f82 45%,#9a7a5c 75%,#3d4a58)"></div>
    <div class="gold-band" style="left:8px;top:221px;width:202px;height:22px;padding-left:6px;font-size:13px;letter-spacing:.4px">HOUSING DEVELOPMENTS</div>
    <div class="copy justify" style="left:16px;top:251px;width:186px">
      <p>At Holvane Builds we don’t just specialise in very high-end residential projects, we also have decades of experience building volume residential housing developments consisting of multiple houses or blocks of apartments.</p>
      <p>Utilising our independently accredited building management systems we have developed we can provide excellent quality control, health and safety and value for housing developers who require the experience and expertise that only a few construction companies can provide.</p>
    </div>
  </div>

  <div class="panel paper" style="width:218px">
    <div class="gold-band" style="left:2px;top:20px;width:216px;height:22px;padding-left:14px;font-size:16px;letter-spacing:1px">LUXURY HOMES</div>
    <div class="copy justify dark" style="left:16px;top:50px;width:172px;font-weight:300;font-size:8.5px;line-height:12.4px">
      <p>At Holvane Builds we are very fortunate to be specialists at working on very high end luxurious residential properties. We work closely with our clients and their design team to build dream homes that are unique, luxurious and architecturally splendid.</p>
      <p style="margin-top:12.4px">Architects and designers will always appreciate the practical input of a construction team that can offer solutions which allow the design concept to be brought to life without compromise.</p>
    </div>
    <div class="photo" role="img" aria-label="Contemporary villa with glass walls and pool overlooking the sea at dusk" style="left:16px;top:238px;width:171px;height:203px;background:linear-gradient(160deg,#2f2b2a,#9c6c45 40%,#c8c3ba 70%,#3f9ac4)"></div>
  </div>
</section>

</body>
</html>
```